Flyer-Design für Seminarreihe „Geldwissen im Erbbetrieb kompakt“
Zielgruppe
MORAVEK FINANCE TRAINING ist mit mehr als 20 Jahren Erfahrung und über 100 Qualifizierungsprojekten ein führender Anbieter für Personalentwicklung. Gleichzeitig beraten wir unter der Marke „MORAVEK CORPORATE FINANCE“ Unternehmen in Ihrem Finanzmanagement. Mehr Informationen unter www.moravek.de.
Nun wollen wir erstmalig eine Seminarreihe für eine neue Zielgruppe anbieten:
Gesellschafter, Beiräte und Führungskräfte von Familienunternehmen durchführen, die keine betriebs- bzw. finanzwirtschaftlichen Ausbildung haben.
Es sollen fünf 1-Tages-Seminare angeboten werden, die die Teilnehmer in die Lage versetzen sollen:
• Unternehmerische Strategien besser zu verstehen, zu hinterfragen und Entscheidungen zu treffen.
• Lesen und Verstehen von Jahresabschlüssen („Bilanzen“), relevanten Finanzkennzahlen und Unternehmensplanungen.
• Grundsätze der Unternehmensführung, so genannte „Corporate Governance“, insbesondere die Zusammenarbeit zwischen, Management und Eigentümern beurteilen.
• Unternehmensbewertung und Strategien der Unternehmensfinanzierung verstehen.
Aufgabenstellung
• Wir benötigen einen Flyer / Broschüre für die Qualifizierungsreihe. Die Inhalte werden gerade von uns erarbeitet und werden von uns geliefert.
• Teil der Ausschreibung ist das Finden eines adressatengerechten „Titels“ bzw. „Slogan“
• Die Hauptaufgabe der Kreativen ist die Entwicklung und die Umsetzung des Layouts!
Rahmenbedingungen/Anforderungen:
• Benutzung des bestehenden Corporate Designs (vgl. Homepage):
• Logo „MORAVEK FINANCE TRAINING“ als Marke
• Verwendung Schrift TransitPrintOT (kann zur Verfügung gestellt werden)
• Verwendung der CD-Farben (Dunkelrot: R 176, G 0, B 51; Dunkelblaugrün: R 1, G 102, B 114, Blaugrün: R 190, G 216, B 219
• Verwendung des Hintergrunds unserer Homepage (bildhain-Lizenz ist vorhanden)
Format:
• Hier sind wir offen für Ihre kreativen Lösungen. Der Flyer wird überwiegend als PDF verschickt.
• Dateiformat: Durch uns verwendbares und editierbares Format.
Claim/Botschaft:
• Siehe oben
• Wir adressieren eine exclusive Klientel und bieten auch im oberen Preissegment an, Durchführung in 5*-Hotel. Dieses „Niveau“ soll das Design wiederspiegeln.
Inhalte Grobstruktur (Arbeitsversion):
1. Cover/ Ansprache der Zielgruppe
2. Idee / Nutzen für Teilnehmer
3. Vorstellung der Trainer und MORAVEK FINANCE TRAINING
4. Die einzelnen Seminare im Überblick (jeweils eine Seite im gleichen Layout)
5. Anmeldeformular

```html
<!DOCTYPE html>
<html lang="de">
<head>
<meta charset="utf-8">
<title>Moravek Finance Training – Seminarreihe Flyer</title>
<link href="https://fonts.googleapis.com/css2?family=Fira+Sans:wght@300;400;500&display=swap" rel="stylesheet">
<style>
:root{
  --stage:#3e3e3e;
  --red:#b00033;
  --band-red:#bd3a58;
  --band-red-dark:#a82e4b;
  --teal:#016672;
  --band-teal:#2f7f8a;
  --band-teal-dark:#1d6b77;
  --teal-light:#bed8db;
  --ink:#2a2a2a;
  --copy:#7a7a7a;
  --rule:#cfcfcf;
  --white:#ffffff;
}
*{box-sizing:border-box;margin:0;padding:0}
html,body{width:1200px;height:2560px;overflow:hidden}
body{background:var(--stage);font-family:"Fira Sans",Arial,sans-serif;font-weight:300;color:var(--copy);position:relative}
.page{position:absolute;left:120px;width:958px;height:480px;background:var(--white);overflow:hidden}
.page--half{width:479px}
.abs{position:absolute}

/* cover */
.cover-photo{position:absolute;left:0;top:0;width:958px;height:370px;
  background:linear-gradient(180deg,#e6e9eb 0%,#d8dcdf 30%,#9ea3a6 52%,#6f7478 70%,#5b6064 100%)}
.cover-headline{position:absolute;left:530px;top:44px;font-size:29px;line-height:36px;font-weight:400;color:var(--ink);letter-spacing:.5px}
.brand{position:absolute;left:806px;top:58px;font-size:13.5px;line-height:17px;font-weight:400;color:var(--teal);letter-spacing:.6px}
.brand-dot{position:absolute;left:890px;top:18px;width:22px;height:22px;border-radius:50%;background:var(--teal)}
.cover-band{position:absolute;left:0;top:370px;width:958px;height:110px;background:linear-gradient(90deg,var(--band-red-dark),var(--band-red) 50%,var(--band-red-dark));border-top:3px solid #3a3a3a}
.band-title{position:absolute;color:var(--white);font-weight:400;letter-spacing:.8px}
.band-rule{position:absolute;height:1px;background:rgba(255,255,255,.8)}
.contact{position:absolute;top:60px;font-size:7.5px;line-height:10px;color:var(--white)}
.contact span{opacity:.8}
.claim-sub{position:absolute;left:530px;top:73px;font-size:8.5px;line-height:12px;color:var(--white);font-weight:400}

/* section headers */
.section-head{position:absolute;left:0;top:0;width:100%;height:92px;border-bottom:4px solid #333}
.section-head--teal{background:linear-gradient(180deg,#3d8b95 0%,var(--band-teal) 55%,var(--band-teal-dark) 100%)}
.section-head--red{background:linear-gradient(180deg,#c95570 0%,var(--band-red) 55%,var(--band-red-dark) 100%)}
.section-title{position:absolute;left:36px;top:36px;font-size:18.5px;font-weight:400;color:var(--white);letter-spacing:1px}
.section-rule{position:absolute;left:0;top:61px;width:428px;height:1px;background:rgba(255,255,255,.85)}
.section-intro{position:absolute;left:517px;top:34px;font-size:9.5px;line-height:12.5px;color:var(--white);font-weight:400}

/* text */
.h-teal{font-size:12.5px;font-weight:400;color:var(--teal);letter-spacing:.4px;margin-bottom:8px}
.copy{font-size:7.5px;line-height:10px;color:var(--copy)}
.copy p{margin-bottom:10px}
.dots{list-style:none;font-size:7.5px;line-height:10px;margin:0 0 10px 10px}
.dots li{position:relative;padding-left:9px}
.dots li::before{content:"";position:absolute;left:0;top:3.5px;width:3px;height:3px;border-radius:50%;background:var(--teal)}
.dots--red li::before{background:var(--red)}
.dots--light li::before{background:var(--white)}

/* welcome */
.portrait{position:absolute;background:linear-gradient(160deg,#5a5a5a,#2a2a2a 60%,#1b1b1b)}
.signature{position:absolute;left:513px;top:302px;width:160px;height:28px;background:#f4f4f4}

/* trainers */
.trainer{position:absolute;width:410px;height:100px}
.trainer .photo{position:absolute;left:0;top:0;width:96px;height:96px;box-shadow:2px 2px 4px rgba(0,0,0,.25)}
.photo--dark{background:linear-gradient(160deg,#6a6a6a,#2b2b2b 65%,#1c1c1c)}
.photo--light{background:linear-gradient(160deg,#f2f2f2,#d9d9d9 50%,#2c3e66 100%)}
.tag{position:absolute;left:107px;top:1px;height:10px;width:46px;background:var(--red);color:var(--white);font-size:7px;line-height:10px;padding-left:3px;font-weight:400}
.trainer .name{position:absolute;left:107px;top:18px;font-size:7.5px;line-height:10px;color:var(--ink);font-weight:400;width:93px;padding-bottom:3px;border-bottom:1px solid var(--red)}
.trainer .fields{position:absolute;left:107px;top:53px;width:150px}
.trainer .facts{position:absolute;left:263px;top:53px;width:140px}
.label{font-size:7.5px;line-height:10px;color:var(--ink);font-weight:400}
.trainer .dots{margin:0 0 0 10px}

/* seminars */
.divider{position:absolute;left:479px;top:96px;width:1px;height:384px;background:#dedede}
.seminar{position:absolute;top:0;width:479px;height:480px}
.seminar-badge{position:absolute;left:36px;top:137px;height:15px;padding:0 4px;background:var(--red);color:var(--white);font-size:11px;line-height:15px;font-weight:400;letter-spacing:.4px}
.seminar-title{position:absolute;left:114px;top:134px;width:330px;font-size:12.5px;line-height:16.5px;color:var(--teal);font-weight:400;letter-spacing:.4px}
.col-label{font-size:7px;color:var(--teal);font-weight:400;letter-spacing:.3px;border-bottom:1px solid var(--teal);display:inline-block;padding-bottom:2px;margin-bottom:8px}
.overview{position:absolute;left:36px;top:343px;width:159px;height:101px;background:linear-gradient(180deg,#3a8891,var(--band-teal-dark));padding:11px 12px;color:var(--white)}
.overview .title{font-size:7px;font-weight:400;letter-spacing:.3px;margin-bottom:9px}
.overview .dots{color:var(--teal-light);margin-left:10px}

/* form */
.form-title{position:absolute;left:36px;top:126px;font-size:12.5px;line-height:16px;color:var(--red);font-weight:400;letter-spacing:.4px}
.choice{position:absolute;left:36px;width:420px;font-size:7.5px;line-height:10px;color:var(--copy)}
.choice .box{position:absolute;left:0;top:1px;width:6px;height:6px;border:1px solid var(--red)}
.choice .text{margin-left:14px;width:260px}
.choice .text b{color:var(--red);font-weight:400}
.choice .price{position:absolute;left:285px;top:0;color:var(--red)}
.form-label{font-size:7px;color:var(--red);font-weight:400;border-bottom:1px solid var(--red);display:inline-block;padding-bottom:2px;width:88px}
.field{position:absolute;left:168px;font-size:7.5px;color:var(--copy)}
.field .line{position:absolute;top:8px;height:1px;background:var(--rule)}
.note{position:absolute;left:36px;top:452px;font-size:5.5px;color:var(--copy)}
</style>
</head>
<body>

<!-- Cover -->
<section class="page" style="top:32px">
  <div class="cover-photo" role="img" aria-label="Luftbild einer Bankenstadt mit Hochhäusern unter bewölktem Himmel"></div>
  <h1 class="cover-headline">EXPERTISE.<br>KOMPETENZ.<br>ERFOLG.</h1>
  <div class="brand-dot"></div>
  <div class="brand">MORAVEK<br>FINANCE TRAINING</div>
  <div class="cover-band" role="img" aria-label="Rot eingefärbtes Stadtbild als Bandhintergrund">
    <div class="band-title" style="left:201px;top:27px;font-size:17px">KONTAKT</div>
    <div class="band-rule" style="left:127px;top:52px;width:218px"></div>
    <div class="contact" style="left:130px;text-align:right;width:72px">MORAVEK GMBH<br><span>Ahornweg 14</span><br><span>D-65195 Wiesbaden</span></div>
    <div class="contact" style="left:259px">Tel. <span>+49 (611) 4470210</span><br>Fax. <span>+49 (611) 4470219</span><br>eMail <span>info@moravek.de</span></div>
    <div class="band-title" style="left:530px;top:14px;font-size:17px;line-height:23px">GELDWISSEN IM ERBBETRIEB<br>KOMPAKT</div>
    <div class="band-rule" style="left:480px;top:60px;width:430px"></div>
    <div class="claim-sub">FACH- UND BERATUNGSKOMPETENZ FÜR<br>CORPORATE BANKING &amp; CORPORATE FINANCE</div>
  </div>
</section>

<!-- Welcome -->
<section class="page" style="top:537px">
  <header class="section-head section-head--teal" role="img" aria-label="Blaugrün eingefärbtes Stadtpanorama">
    <h2 class="section-title">WILLKOMMEN BEI MORAVEK FINANCE TRAINING</h2>
    <div class="section-rule"></div>
    <p class="section-intro">MORAVEK FINANCE TRAINING ist mit mehr als 20 Jahren Erfahrung und über<br>100 Qualifizierungsprojekten ein führender Anbieter für Personalentwicklung.</p>
  </header>
  <div class="abs" style="left:36px;top:122px;width:305px">
    <h3 class="h-teal">ÜBER MORAVEK</h3>
    <div class="copy"><p>Epratemperum quam, cum eum fugit, excerio et eaque plabo. Et ut fugitat voluptur autes est rehendicius cuptat. Optas ent etum et velenih illatior reium sectione labo. Rum laturitem. Re aute cumquiat faccae verum, etus ipsam debita antis mo od quo est maximpo rendaero quae expliquis moloreiur?</p></div>
    <h3 class="h-teal" style="margin-top:14px">EIN EINZIGARTIGES SCHULUNGSKONZEPT</h3>
    <div class="copy">
      <p>Mi, tem et ea se consequiam am dolore audaeptatur mos remqui tem est eiumquis con rehenis sapicip isquat.</p>
      <p>Eceperio. Faces rem incipsa aut volor aspienis res exeri undit evenda doluptur? Orem inumquodi ab ipsandae. Itatus num hitasimus aliasi solorest eicipsam fugit et lacilla ceperum velecum quia solupta que ped excest, is sument aligenectae cuptatur, si bea etus moloreceproqui officitibus.</p>
    </div>
    <ul class="dots"><li>Aufzählung 1</li><li>Aufzählung 2</li><li>Aufzählung 3</li></ul>
    <div class="copy"><p>Otatiori utem latusam, conetus, cone et aditam, optatur?</p>
    <p>Exere porum dolecum, velluptate vent haria dus explis dolo volores milliquatem endam ersperumqui quis aut et volor aut et qui veligen damenis ni dolorum, cusapel lecatem quidesti officitempora sanis eume nobis sumquis acere poraeritae qui dusandis ex eat maios cum si alite velitem assequi undestr undistotas ratquidus.</p></div>
  </div>
  <div class="abs" style="left:517px;top:122px;width:300px">
    <h3 class="h-teal">EXPERTISE. KOMPETENZ. ERFOLG.</h3>
    <div class="copy"><p>Epratemperum quam, cum eum fugit, excerio et eaque plabo. Et ut fugitat voluptur autes est rehendicius cuptat. Optas ent etum et velenih illatior reium sectione labo. Rum laturitem. Re aute cumquiat faccae verum, etus ipsam debita antis mo od quo est maximpo rendaero quae expliquis moloreiur?</p>
    <p>Mi, tem et ea se consequiam am dolore audaeptatur mos remqui tem est eiumquis con rehenis sapicip isquat. Eceperio. Faces rem incipsa aut volor aspienis res exeri undit evenda doluptur? Orem inumquodi ab ipsandae. Itatus num hitasimus aliasi solorest eicipsam fugit et lacilla ceperum velecum quia solupta que ped excest, is sument aligenectae cuptatur, si bea etus moloreceproqui officitibus.</p>
    <p style="margin-top:14px">Viel Vergnügen mit der Seminarreihe wünscht Ihnen</p></div>
  </div>
  <div class="signature" role="img" aria-label="Handschriftliche Unterschrift des Geschäftsführers"></div>
  <div class="copy abs" style="left:517px;top:338px">Max Mustermann<br>Geschäftsführer Moravek GmbH</div>
  <div class="portrait" style="left:793px;top:270px;width:157px;height:210px" role="img" aria-label="Porträtfoto des Geschäftsführers im Anzug"></div>
</section>

<!-- Trainers -->
<section class="page" style="top:1040px">
  <header class="section-head section-head--red" role="img" aria-label="Rot eingefärbtes Stadtpanorama">
    <h2 class="section-title">UNSERE TRAINER/INNEN</h2>
    <div class="section-rule"></div>
    <p class="section-intro">Kompetent, freundlich und professionell:<br>die drei Kernkompetenzen unserer engagierten Trainer/innen.</p>
  </header>

  <article class="trainer" style="left:36px;top:117px">
    <div class="photo photo--dark" role="img" aria-label="Porträtfoto Trainer"></div>
    <div class="tag">TRAINER</div>
    <div class="name">Dr. Max<br>MUSTERMANN</div>
    <div class="fields"><div class="label">Experte auf den Gebieten:</div><ul class="dots dots--red copy"><li>Unternehmensbewertung</li><li>M&amp;A Beratung</li><li>Unternehmsgründung</li><li>Unternehmensnachfolge</li></ul></div>
    <div class="facts"><div class="label">Wissenswertes:</div><div class="copy">7 Jahre bei Firma xy gearbeitet, langjährige Kompetenz im Bereich der Kreditwirtschaft und des Finanzmanagements.</div></div>
  </article>
  <article class="trainer" style="left:517px;top:117px">
    <div class="photo photo--light" role="img" aria-label="Porträtfoto Coach"></div>
    <div class="tag">COACH</div>
    <div class="name">Maxime<br>MUSTERFRAU, MA MBA</div>
    <div class="fields"><div class="label">Expertin auf den Gebieten:</div><ul class="dots dots--red copy"><li>Bankenmanagement &amp; Rating</li><li>Unternehmsgründung</li><li>Strategische Investorensuche</li></ul></div>
    <div class="facts"><div class="label">Wissenswertes:</div><div class="copy">Jahrelanges Know-How im Bereich Bankenmanagement aufgebaut. 10 Jahre bei Firma xy gearbeitet.</div></div>
  </article>
  <article class="trainer" style="left:36px;top:233px">
    <div class="photo photo--light" role="img" aria-label="Porträtfoto Trainerin"></div>
    <div class="tag">TRAINERIN</div>
    <div class="name">Maxime<br>MUSTERFRAU, MA MBA</div>
    <div class="fields"><div class="label">Expertin auf den Gebieten:</div><ul class="dots dots--red copy"><li>Bankenmanagement &amp; Rating</li><li>Unternehmsgründung</li><li>Strategische Investorensuche</li></ul></div>
    <div class="facts"><div class="label">Wissenswertes:</div><div class="copy">Jahrelanges Know-How im Bereich Bankenmanagement aufgebaut. 10 Jahre bei Firma xy gearbeitet.</div></div>
  </article>
  <article class="trainer" style="left:517px;top:233px">
    <div class="photo photo--dark" role="img" aria-label="Porträtfoto Berater"></div>
    <div class="tag">BERATER</div>
    <div class="name">Dr. Max<br>MUSTERMANN</div>
    <div class="fields"><div class="label">Experte auf den Gebieten:</div><ul class="dots dots--red copy"><li>Unternehmensbewertung</li><li>M&amp;A Beratung</li><li>Unternehmsgründung</li><li>Unternehmensnachfolge</li></ul></div>
    <div class="facts"><div class="label">Wissenswertes:</div><div class="copy">7 Jahre bei Firma xy gearbeitet, langjährige Kompetenz im Bereich der Kreditwirtschaft und des Finanzmanagements.</div></div>
  </article>
  <article class="trainer" style="left:36px;top:349px">
    <div class="photo photo--dark" role="img" aria-label="Porträtfoto Trainer"></div>
    <div class="tag">TRAINER</div>
    <div class="name">Dr. Max<br>MUSTERMANN</div>
    <div class="fields"><div class="label">Experte auf den Gebieten:</div><ul class="dots dots--red copy"><li>Unternehmensbewertung</li><li>M&amp;A Beratung</li><li>Unternehmsgründung</li><li>Unternehmensnachfolge</li></ul></div>
    <div class="facts"><div class="label">Wissenswertes:</div><div class="copy">7 Jahre bei Firma xy gearbeitet, langjährige Kompetenz im Bereich der Kreditwirtschaft und des Finanzmanagements.</div></div>
  </article>
  <article class="trainer" style="left:517px;top:349px">
    <div class="photo photo--light" role="img" aria-label="Porträtfoto Trainerin"></div>
    <div class="tag">TRAINERIN</div>
    <div class="name">Maxime<br>MUSTERFRAU, MA MBA</div>
    <div class="fields"><div class="label">Expertin auf den Gebieten:</div><ul class="dots dots--red copy"><li>Bankenmanagement &amp; Rating</li><li>Unternehmsgründung</li><li>Strategische Investorensuche</li></ul></div>
    <div class="facts"><div class="label">Wissenswertes:</div><div class="copy">Jahrelanges Know-How im Bereich Bankenmanagement aufgebaut. 10 Jahre bei Firma xy gearbeitet.</div></div>
  </article>
</section>

<!-- Seminar program -->
<section class="page" style="top:1545px">
  <header class="section-head section-head--teal" role="img" aria-label="Blaugrün eingefärbtes Stadtpanorama">
    <h2 class="section-title">DAS SEMINARPROGRAMM</h2>
    <div class="section-rule"></div>
    <p class="section-intro">Es erwarten Sie vielseitige und lehrreiche 1-Tages-Seminare.<br>Nutzen Sie die Chance und vergrößern Sie Ihr Wissen rund um die Welt der Finanzen.</p>
  </header>
  <div class="divider"></div>

  <article class="seminar" style="left:0">
    <div class="seminar-badge">SEMINAR 1</div>
    <h3 class="seminar-title">UNTERNEHMERISCHE STRATEGIEN BESSER ZU VERSTEHEN, ZU HINTERFRAGEN UND ENTSCHEIDUNGEN ZU TREFFEN.</h3>
    <div class="abs copy" style="left:36px;top:203px;width:188px"><div class="col-label">KURZBESCHREIBUNG:</div>
      <p>Dieses Seminar behandelt ... Eceperio. Faces rem incipsa aut volor aspienis res exeri undit evenda doluptur?</p>
      <p>Orem inumquodi ab ipsandae. Itatus num hitasimus aliasi solorest eicipsam fugit et lacilla ceperum velecum quia solupta que ped excest, is sument aligenectae cuptatur, si bea etus moloreceproqui officitibus.</p></div>
    <div class="abs copy" style="left:245px;top:203px;width:200px"><div class="col-label">SEMINARINHALTE IM DETAIL:</div>
      <p>Encipsa aut volor aspienis res exeri undit evenda doluptur? Orem inumquodi ab ipsandae. Itatus num hitasimus aliasi solorest eicipsam fugit et lacilla ceperum velecum quia solupta que ped excest, is sument aligenectae cuptatur, si bea etus moloreceproqui officitibus.</p>
      <p>Orem inumquodi ab ipsandae. Itatus num hitasimus aliasi solorest eicipsam fugit et lacilla ceperum velecum quia solupta que ped excest, is sument aligenectae cuptatur, si bea etus moloreceproqui officitibus.</p>
      <p>Mi, tem et ea se consequiam am dolore audaeptatur mos remqui tem est eiumquis con rehenis sapicip isquat. Eceperio. Faces rem incipsa aut volor aspienis res exeri undit evenda doluptur? Orem inumquodi ab ipsandae. Itatus num hitasimus aliasi solorest eicipsam fugit et lacilla ceperum velecum quia solupta que ped excest, is sument aligenectae cuptatur, si bea etus moloreceproqui officitibus.</p></div>
    <div class="overview"><div class="title">SEMINARINHALTE IM ÜBERBLICK:</div>
      <ul class="dots dots--light copy"><li>Seminarinhalt 1</li><li>Seminarinhalt 2</li><li>Seminarinhalt 3</li><li>Seminarinhalt 4</li><li>Seminarinhalt 5</li><li>Seminarinhalt 6</li></ul></div>
  </article>

  <article class="seminar" style="left:481px">
    <div class="seminar-badge">SEMINAR 2</div>
    <h3 class="seminar-title">LESEN UND VERSTEHEN VON JAHRESABSCHLÜSSEN („BILANZEN“), RELEVANTEN FINANZKENNZAHLEN UND UNTERNEHMENSPLANUNGEN.</h3>
    <div class="abs copy" style="left:36px;top:203px;width:195px"><div class="col-label">KURZBESCHREIBUNG:</div>
      <p>Dieses Seminar behandelt ... Eceperio. Faces rem incipsa aut volor aspienis res exeri undit evenda doluptur?</p>
      <p>Orem inumquodi ab ipsandae. Itatus num hitasimus aliasi solorest eicipsam fugit et lacilla ceperum velecum quia solupta que ped excest, is sument aligenectae cuptatur, si bea etus moloreceproqui officitibus.</p></div>
    <div class="abs copy" style="left:245px;top:203px;width:200px"><div class="col-label">SEMINARINHALTE IM DETAIL:</div>
      <p>Encipsa aut volor aspienis res exeri undit evenda doluptur? Orem inumquodi ab ipsandae. Itatus num hitasimus aliasi solorest eicipsam fugit et lacilla ceperum velecum quia solupta que ped excest, is sument aligenectae cuptatur, si bea etus moloreceproqui officitibus.</p>
      <p>Orem inumquodi ab ipsandae. Itatus num hitasimus aliasi solorest eicipsam fugit et lacilla ceperum velecum quia solupta que ped excest, is sument aligenectae cuptatur, si bea etus moloreceproqui officitibus.</p>
      <p>Mi, tem et ea se consequiam am dolore audaeptatur mos remqui tem est eiumquis con rehenis sapicip isquat. Eceperio. Faces rem incipsa aut volor aspienis res exeri undit evenda doluptur? Orem inumquodi ab ipsandae. Itatus num hitasimus aliasi solorest eicipsam fugit et lacilla ceperum velecum quia solupta que ped excest, is sument aligenectae cuptatur, si bea etus moloreceproqui officitibus.</p></div>
    <div class="overview"><div class="title">SEMINARINHALTE IM ÜBERBLICK:</div>
      <ul class="dots dots--light copy"><li>Seminarinhalt 1</li><li>Seminarinhalt 2</li><li>Seminarinhalt 3</li><li>Seminarinhalt 4</li><li>Seminarinhalt 5</li><li>Seminarinhalt 6</li></ul></div>
  </article>
</section>

<!-- Registration form -->
<section class="page page--half" style="top:2049px">
  <header class="section-head section-head--red" role="img" aria-label="Rot eingefärbtes Stadtpanorama">
    <h2 class="section-title">ANMELDEFORMULAR</h2>
    <div class="section-rule"></div>
  </header>
  <h3 class="form-title">HIERMIT, MÖCHTE ICH MICH ZU FOLGENDEN<br>SEMINAREN ANMELDEN (bitte ankreuzen):</h3>

  <div class="choice" style="top:178px"><span class="box"></span><div class="text"><b>SEMINAR 1:</b> Unternehmerische Strategien besser zu verstehen, zu hinterfragen und Entscheidungen zu treffen.</div><span class="price">€ &nbsp;780,-</span></div>
  <div class="choice" style="top:208px"><span class="box"></span><div class="text"><b>SEMINAR 2:</b> Lesen und Verstehen von Jahresabschlüssen („Bilanzen“), relevanten Finanzkennzahlen und Unternehmensplanungen.</div><span class="price">€ &nbsp;780,-</span></div>
  <div class="choice" style="top:238px"><span class="box"></span><div class="text"><b>SEMINAR 3:</b> Titel des dritten Seminars kommt hierhin</div><span class="price">€ &nbsp;780,-</span></div>
  <div class="choice" style="top:258px"><span class="box"></span><div class="text"><b>SEMINAR 4:</b> Titel des vierten Seminars kommt hierhin</div><span class="price">€ &nbsp;780,-</span></div>
  <div class="choice" style="top:278px"><span class="box"></span><div class="text"><b>SEMINAR 5:</b> Titel des fünften Seminars kommt hierhin</div><span class="price">€ &nbsp;780,-</span></div>

  <div class="abs copy" style="left:36px;top:312px">
    <div class="form-label">VERANSTALTUNGSORT:</div>
    <p style="margin-top:8px">Moravek GmbH<br>Ahornweg 14<br>D-65195 Wiesbaden</p>
    <p>2. Stock, Seminarraum 1</p>
  </div>
  <div class="abs" style="left:168px;top:312px"><div class="form-label">ANMELDEDATEN:</div></div>
  <div class="field" style="top:343px">Titel:<span class="line" style="left:49px;width:84px"></span></div>
  <div class="field" style="top:363px">Name:<span class="line" style="left:49px;width:228px"></span></div>
  <div class="field" style="top:383px">Firma:<span class="line" style="left:49px;width:228px"></span></div>
  <div class="field" style="top:403px">Adresse:<span class="line" style="left:49px;width:228px"></span></div>
  <div class="field" style="top:423px">PLZ:<span class="line" style="left:49px;width:42px"></span><span style="position:absolute;left:119px;top:0">Ort:</span><span class="line" style="left:155px;width:122px"></span></div>
  <div class="field" style="top:443px">Unterschrift:<span class="line" style="left:49px;width:228px"></span></div>
  <div class="note">Preise netto, exkl. MWST</div>
</section>

</body>
</html>
```